Letterhead designs for Property Management firm

Would like to see some different letterhead/envelope designs We are a residential property management company. We would like to see designs that utilize blue/grays/black

```html
<!DOCTYPE html>
<html lang="en">
<head>
<meta charset="utf-8">
<title>Harborview Property Management – Stationery</title>
<link href="https://fonts.googleapis.com/css2?family=Arimo:wght@400;700&display=swap" rel="stylesheet">
<style>
  :root {
    --blue: #1b53a0;
    --blue-deep: #0b3b80;
    --ink: #1c1c1c;
    --ink-soft: #333333;
    --paper: #ffffff;
    --backdrop: #f1f2f3;
    --edge: #dcdfe3;
  }
  * { box-sizing: border-box; margin: 0; padding: 0; }
  html, body { width: 1200px; height: 913px; overflow: hidden; }
  body {
    position: relative;
    background: radial-gradient(ellipse at 50% 50%, #ffffff 55%, var(--backdrop) 100%);
    font-family: "Arimo", Arial, sans-serif;
    color: var(--ink);
  }

  /* Brand block: name as text with one plain square */
  .brand {
    display: flex; align-items: center; gap: 8px;
    color: var(--blue); font-weight: 700; line-height: 1.15;
  }
  .brand-square { background: var(--blue); flex: none; }
  .brand-name { display: block; }

  /* Plain bands */
  .band { position: absolute; left: 0; right: 0; }
  .band-main { background: var(--blue); }
  .band-rule { background: var(--blue-deep); }

  /* Envelope */
  .envelope {
    position: absolute; left: 195px; top: 357px;
    width: 381px; height: 202px;
    background: var(--paper);
    border: 1px solid var(--edge);
    overflow: hidden;
  }
  .envelope .band-main { top: 0; height: 12px; }
  .envelope .band-rule { top: 15px; height: 2px; }
  .envelope .band-foot { bottom: 0; height: 6px; background: var(--blue); }
  .envelope .brand { position: absolute; left: 30px; top: 70px; font-size: 11px; }
  .envelope .brand-square { width: 14px; height: 14px; }
  .envelope-address {
    position: absolute; left: 30px; top: 128px; width: 110px;
    text-align: center; color: var(--ink); line-height: 1.2;
  }
  .envelope-address .line-1 { font-size: 8.5px; }
  .envelope-address .line-2 { font-size: 6px; }
  .envelope-address .line-3 { font-size: 4px; }

  /* Letterhead */
  .letterhead {
    position: absolute; left: 637px; top: 80px;
    width: 514px; height: 775px;
    background: var(--paper);
    border: 1px solid var(--edge);
    overflow: hidden;
  }
  .letterhead .band-main { top: 0; height: 22px; }
  .letterhead .band-rule { top: 27px; height: 3px; }
  .letterhead .band-foot { bottom: 0; height: 14px; background: var(--blue); }
  .letterhead .brand {
    position: absolute; left: 300px; top: 100px; width: 190px; font-size: 15px;
  }
  .letterhead .brand-square { width: 22px; height: 22px; }
  .salutation { position: absolute; left: 48px; top: 200px; }
  .salutation-name { font-size: 19.5px; font-weight: 700; color: var(--ink-soft); }
  .salutation-title { font-size: 12px; margin-left: 67px; margin-top: 4px; }
  .letter-body {
    position: absolute; left: 48px; top: 262px; width: 418px;
    height: 440px; overflow: hidden;
    font-size: 16.3px; line-height: 20.5px; color: var(--ink);
  }
  .letter-body p + p { margin-top: 20.5px; }
</style>
</head>
<body>

  <section class="envelope" aria-label="Envelope">
    <div class="band band-main"></div>
    <div class="band band-rule"></div>
    <div class="band band-foot"></div>
    <div class="brand">
      <span class="brand-square"></span>
      <span><span class="brand-name">HARBORVIEW</span><span class="brand-name">PROPERTY MGMT</span></span>
    </div>
    <div class="envelope-address">
      <div class="line-1">YOUR ADDRESS</div>
      <div class="line-2">YOUR ADDRESS</div>
      <div class="line-3">YOUR ADDRESS</div>
    </div>
  </section>

  <article class="letterhead" aria-label="Letterhead">
    <div class="band band-main"></div>
    <div class="band band-rule"></div>
    <div class="band band-foot"></div>

    <div class="brand">
      <span class="brand-square"></span>
      <span><span class="brand-name">HARBORVIEW</span><span class="brand-name">PROPERTY MANAGEMENT</span></span>
    </div>

    <header class="salutation">
      <div class="salutation-name">Dear Alan Porter</div>
      <div class="salutation-title">Manager Director</div>
    </header>

    <div class="letter-body">
      <p>His was not how Martin Hale or Owen Brandt would have scripted it. A feelgood movie about a veteran editor at the end of his career would have had the hero stepping down at the climax of his last and greatest campaign. The gnarled but lovable chief would write his final triumphalist headline before parading out of the office to a schmaltzy mix of applause and tears.</p>
      <p>And maybe that is how Victor Lane imagined the end of his 26-year tenure of the Morning Ledger. He would stay in the job just long enough to drive a final stake through the heart of Britain’s relationship with Europe. It would be the crowning moment of glory to round off a long and remarkable newspaper career.</p>
      <p>But for that script to work Lane had to stay in post until at least November. He would steer the newspaper through the treacherous shifting sands of Brexit this autumn and be there to stiffen the</p>
    </div>
  </article>

</body>
</html>
```